New young doctors office business card

Doctor's office
Hello:
My name is Dr. Eduardo Maximino Ortega Benavides. I need a business card for my new office located within a hospital. The name of the hospital is "Hospital Almendral". Although the hospital logo and name must be included in the business card, please make me a personal logo for myself. The logo might be maybe my name in a stylish font, or my initials (EMOB) or something like that. Im more inclined to a font logo, rather than a image logo, but a good one might change my mind. The info on my business card is going to be in spanish. The following info must be included please (the info within parenthesis is not to be included, it is provided for you to understand it since it's in spanish, so you can properly place it on the card):
-Dr. Eduardo Maximino Ortega Benavides (my name)
-Medicina general (My specialty)
-Hospital Almendral (The name of the hospital where my office is)
-Calle Tomás Ocampo #247 Col. Almendral (address)
-Tel 471-5836 (Office phone)
-Sábado y domingo 10:00 am a 10:00pm (Office hours)
-Emergencias: 555-917-4402 (Emergency phone)
-maximinoob@correoficticio.mx (email)
-English Spoken
So, that's all the info i need to be on the business card. Although it's a business card for a doctor's office, i dont want it to be a boring, plain business card. Make it eye-catchy and stylish please. As i said, the hospital logo must be included. You'll find it on the heading of the PDF file i attached, but dont make it the center of attention.
Physician
Hello:My name is Dr. Eduardo Maximino Ortega Benavides. I need a business card for my new office located within a hospital. The name of the hospital is "Hospital Almendral". Although the hospital logo and name must be included in the business card, please make me a personal logo for myself. The logo might be maybe my name in a stylish font, or my initials (EMOB) or something like that. Im more inclined to a font logo, rather than a image logo, but a good one might change my mind. The info on my business card is going to be in spanish. The following info must be included please (the info within parenthesis is not to be included, it is provided for you to understand it since it's in spanish, so you can properly place it on the card):-Dr. Eduardo Maximino Ortega Benavides (my name)-Medicina general (My specialty)-Hospital Almendral (The name of the hospital where my office is)-Calle Tomás Ocampo #247 Col. Almendral (address)-Tel 471-5836 (Office phone)-Sábado y domingo 10:00 am a 10:00pm (Office hours)-Emergencias: 555-917-4402 (Emergency phone)-maximinoob@correoficticio.mx (email)-English Spoken So, that's all the info i need to be on the business card. Although it's a business card for a doctor's office, i dont want it to be a boring, plain business card. Make it eye-catchy and stylish please. As i said, the hospital logo must be included. You'll find it on the heading of the PDF file i attached, but dont make it the center of attention.

```html
<!DOCTYPE html>
<html lang="es">
<head>
<meta charset="utf-8">
<title>Tarjeta – Dr. Eduardo Maximino Ortega Benavides</title>
<link rel="stylesheet" href="https://fonts.googleapis.com/css2?family=Open+Sans:wght@400;700&family=Encode+Sans+Condensed:wght@600;700&display=swap">
<style>
  :root{
    --navy:#0b1ba6;
    --navy-deep:#0c1a9a;
    --sky:#4fd3f6;
    --orange:#f26b1d;
    --white:#ffffff;
    --ink:#1b1b2a;
    --emblem-tone:#2a3cc0;
    --metal-light:#d9dde2;
    --metal-dark:#4a4f57;
  }
  html,body{margin:0;padding:0;overflow:hidden;background:var(--white);}
  .card{position:relative;width:1043px;height:1200px;overflow:hidden;background:var(--white);font-family:"Open Sans",Arial,sans-serif;}

  /* front panel */
  .front{position:absolute;left:0;top:0;width:1043px;height:596px;background:var(--navy);}
  .front__emblem{position:absolute;left:300px;top:76px;width:412px;height:392px;border-radius:24px;background:var(--emblem-tone);}
  .front__name{position:absolute;left:0;right:0;top:482px;text-align:center;color:var(--white);
    font-family:"Encode Sans Condensed","Arial Narrow",sans-serif;font-weight:700;font-size:39px;letter-spacing:-0.3px;}

  /* back panel */
  .monogram{position:absolute;left:50px;top:670px;width:215px;text-align:center;color:var(--orange);
    font-family:"Open Sans",Arial,sans-serif;font-weight:700;font-size:54px;line-height:70px;letter-spacing:1px;}
  .title-bar{position:absolute;left:281px;top:659px;width:762px;height:100px;background:var(--navy-deep);color:var(--white);box-sizing:border-box;padding:14px 0 0 22px;}
  .title-bar__name{font-weight:700;font-size:28.5px;line-height:38px;}
  .title-bar__specialty{font-weight:400;font-size:28px;line-height:36px;}

  .instrument{position:absolute;left:50px;top:808px;width:222px;height:198px;border-radius:50% 40% 45% 45%;
    background:linear-gradient(160deg,var(--metal-light),var(--metal-dark));}

  .hospital{position:absolute;left:374px;top:852px;}
  .hospital__mark{position:absolute;left:0;top:2px;width:104px;height:72px;background:var(--navy);}
  .hospital__name{position:absolute;left:120px;top:0;white-space:nowrap;color:var(--navy);font-weight:700;font-size:34px;line-height:44px;}
  .hospital__address{position:absolute;left:120px;top:46px;white-space:nowrap;color:var(--navy);
    font-family:"Encode Sans Condensed","Arial Narrow",sans-serif;font-weight:600;font-size:20.5px;line-height:26px;}

  .tab{position:absolute;left:340px;top:990px;width:442px;height:80px;background:var(--white);
    border-bottom:11px solid var(--navy);border-radius:0 0 44px 44px;box-sizing:content-box;z-index:2;}
  .band{position:absolute;left:0;top:1014px;width:1043px;height:20px;background:var(--navy);}
  .footer{position:absolute;left:0;top:1034px;width:1043px;height:166px;background:var(--sky);}

  .contact{position:absolute;left:378px;top:942px;z-index:3;color:var(--ink);font-size:24px;line-height:35px;}
  .contact__row{position:relative;padding-left:56px;white-space:nowrap;}
  .contact__label{display:inline-block;width:148px;}
  .contact__icon{position:absolute;left:0;width:40px;height:40px;background:var(--orange);}
  .contact__icon svg{display:block;width:40px;height:40px;}
  .contact__row--email{margin-top:4px;}

  .footer__lang{position:absolute;left:0;right:0;top:1100px;text-align:center;color:var(--ink);font-size:24px;}
  .footer__hours{position:absolute;left:0;right:0;top:1130px;text-align:center;color:var(--white);font-size:29px;}
  .footer__lang,.footer__hours{padding-left:36px;}
</style>
</head>
<body>
<main class="card">
  <section class="front">
    <div class="front__emblem" role="img" aria-label="Emblema médico blanco: caduceo con alas y serpientes"></div>
    <div class="front__name">Dr. Eduardo Maximino Ortega Benavides</div>
  </section>

  <section class="back">
    <div class="monogram">EMOB</div>
    <div class="title-bar">
      <div class="title-bar__name">Dr. Eduardo Maximino Ortega Benavides</div>
      <div class="title-bar__specialty">Medicina general</div>
    </div>

    <div class="instrument" role="img" aria-label="Fotografía de un estetoscopio negro y plateado"></div>

    <div class="hospital">
      <div class="hospital__mark"></div>
      <div class="hospital__name">Hospital Almendral</div>
      <div class="hospital__address">Calle Tomás Ocampo #247 Col. Almendral</div>
    </div>

    <div class="band"></div>
    <div class="footer"></div>
    <div class="tab"></div>

    <div class="contact">
      <div class="contact__row">
        <span class="contact__icon" style="top:4px">
          <svg viewBox="0 0 40 40" aria-hidden="true"><path d="M14 9c1.5-1 3-.6 3.6.8l1.6 3.8c.5 1.2 0 2.2-1 2.9l-1.4 1c.9 2.4 2.6 4.4 4.8 5.8l1.1-1.3c.8-.9 1.9-1.2 3-.6l3.6 1.9c1.3.7 1.5 2.3.4 3.6-1.6 2-3.9 2.8-6.3 1.8C17.1 26.6 13.2 22 11.6 16.6 10.9 13.6 11.8 10.8 14 9z" fill="#fff"/></svg>
        </span>
        <span class="contact__label">Office</span>: 656-471-5836
      </div>
      <div class="contact__row"><span class="contact__label">Emergency</span>: 555-917-4402</div>
      <div class="contact__row contact__row--email">
        <span class="contact__icon" style="top:-2px">
          <svg viewBox="0 0 40 40" aria-hidden="true"><rect x="8" y="12" width="24" height="16" fill="none" stroke="#fff" stroke-width="2.4"/><path d="M8 12l12 9 12-9M8 28l9-8M32 28l-9-8" fill="none" stroke="#fff" stroke-width="2.4"/></svg>
        </span>
        maximinoob@correoficticio.mx
      </div>
    </div>

    <div class="footer__lang">English Spoken</div>
    <div class="footer__hours">Sábado y domingo 10.00am a 10.00pm</div>
  </section>
</main>
</body>
</html>
```